Vendor Managed Inventory Talking points/Customer hand out

Looking for a single page flyer/Customer handout to be a sell sheet for our Vendor managed Inventory programs
Title: VMI benefits
Risk management:
Identification of Items and values that are sole sourced
Ongoing plans to reduce exposure to sole sourced items
Schedule planning to eliminate freight and outages
Reducing the hidden costs of forecasting errors
(Note; with us managing the point of use we can more accurately forecast)
Managing ever shortening of product lifecycles, minimizing obsolescence
Zero Inventory Exposure:
Minimized or Zero inventory on commodity items
Greatly reducing the Weighted Cost of Capital (WACC)
Reduced WACC can help in calculating Hurdle Rates
True point of use billing:
Allows for better tracking and allocation of expenses from a job-job basis
Custom labeling:
Including things like customer part numbers, exp dates, internal hazmat codes
Insures accurate processes with current materials
Helps to meet 5S requirements
Required for certain audits
Lot tracking/Shelf life:
Active assistance in managing Date Codes/Lot Tracking
Shortened shelf life products identified and managed
Plain statement of expiration dates on products. Calculations are not required
Taken as a whole we can help calculate TRUE management and landed costs of products. Focusing only on the price of items is like looking at just the exposed part of an iceberg. Let RT7K help you to see what's underneath.
I have attached some other brochures and flyers for style reference
more info on our website too. www.rt7k-example.com
Target Market(s)
Electronics manufacturers
Industry/Entity Type
Electronics
Look and feel

```html
<!DOCTYPE html>
<html lang="en">
<head>
<meta charset="utf-8">
<title>VMI Benefits – RT7K</title>
<link href="https://fonts.googleapis.com/css2?family=Oswald:wght@500;600&family=Open+Sans:wght@400;700&display=swap" rel="stylesheet">
<style>
  :root {
    --brand-blue: #1c4f8e;
    --brand-blue-deep: #153f75;
    --paper: #ffffff;
    --ink-light: #e8eef7;
    --photo-dark: #3a3d42;
    --photo-light: #b9bcc0;
  }
  * { margin: 0; padding: 0; box-sizing: border-box; }
  html, body { width: 801px; height: 1200px; overflow: hidden; background: var(--paper); }
  .flyer { position: relative; width: 801px; height: 1200px; overflow: hidden; background: var(--brand-blue); }
  .flyer-art { position: absolute; inset: 0; width: 801px; height: 1060px; }
  .brand-name {
    position: absolute; top: 22px; right: 44px;
    font-family: "Oswald", sans-serif; font-weight: 600; font-size: 50px; letter-spacing: 2px;
    color: var(--brand-blue);
  }
  .title {
    position: absolute; left: 40px; top: 462px;
    font-family: "Oswald", sans-serif; font-weight: 500; font-size: 86px; line-height: 94px;
    color: var(--paper); text-transform: uppercase;
  }
  .benefits { position: absolute; top: 680px; left: 43px; right: 30px; display: grid; grid-template-columns: 448px 1fr; }
  .benefit { margin-bottom: 12px; }
  .benefit h2 {
    font-family: "Oswald", sans-serif; font-weight: 500; font-size: 23px; line-height: 28px;
    color: var(--paper); text-transform: uppercase;
  }
  .benefit p {
    font-family: "Open Sans", sans-serif; font-size: 14.5px; line-height: 21px; color: var(--ink-light);
  }
  .summary {
    position: absolute; top: 1060px; left: 0; width: 801px; height: 58px; background: var(--paper);
    display: flex; align-items: center; justify-content: center; text-align: center;
    font-family: "Open Sans", sans-serif; font-weight: 700; font-size: 13.5px; line-height: 19px;
    color: var(--brand-blue-deep); padding: 0 30px;
  }
  .contact-bar {
    position: absolute; top: 1118px; left: 0; width: 801px; height: 82px;
    display: flex; align-items: center; justify-content: center; gap: 18px;
    font-family: "Oswald", sans-serif; font-weight: 500; font-size: 36px; color: var(--paper);
  }
</style>
</head>
<body>
<main class="flyer">
  <svg class="flyer-art" viewBox="0 0 801 1060" aria-hidden="false">
    <defs>
      <linearGradient id="storeroomTones" x1="0" y1="0" x2="1" y2="1">
        <stop offset="0" stop-color="var(--photo-dark)"/>
        <stop offset="0.55" stop-color="#8a8e94"/>
        <stop offset="1" stop-color="var(--photo-light)"/>
      </linearGradient>
    </defs>
    <rect role="img" aria-label="Photo of a stockroom with shelving full of parts bins" x="0" y="0" width="801" height="640" fill="url(#storeroomTones)"/>
    <path class="logo-arc" d="M 480 0 Q 600 120 801 95 L 801 0 Z" fill="var(--paper)"/>
    <path class="swoosh" d="M 0 265 Q 330 520 801 618 L 801 1060 L 0 1060 Z" fill="var(--brand-blue)"/>
  </svg>

  <div class="brand-name">RT7K</div>

  <h1 class="title">VMI<br>Benefits</h1>

  <section class="benefits">
    <div class="benefit-column">
      <article class="benefit">
        <h2>Risk Management:</h2>
        <p>Identification of Items and values that are sole sourced<br>
        Ongoing plans to reduce exposure to sole sourced items<br>
        Schedule planning to eliminate freight and outages<br>
        Reducing the hidden costs of forecasting errors<br>
        (Note; with us managing the point of use we can more accurately forecast)<br>
        Managing ever shortening of product lifecycles, minimizing obsolescence</p>
      </article>
      <article class="benefit">
        <h2>Custom Labeling:</h2>
        <p>Including things like customer part numbers, exp dates, internal hazmat codes<br>
        Insures accurate processes with current materials<br>
        Helps to meet 5S requirements<br>
        Required for certain audits</p>
      </article>
    </div>
    <div class="benefit-column">
      <article class="benefit">
        <h2>Zero Inventory Exposure:</h2>
        <p>Minimized or Zero inventory on commodity items<br>
        Greatly reducing the Weighted Cost of Capital (WACC)<br>
        Reduced WACC can help in calculating Hurdle Rates</p>
      </article>
      <article class="benefit">
        <h2>True Point of Use Billing:</h2>
        <p>Allows for better tracking and allocation of expenses from a job-job basis</p>
      </article>
      <article class="benefit">
        <h2>Lot Tracking/Shelf Life:</h2>
        <p>Active assistance in managing Date Codes/Lot Tracking. Shortened shelf life products identified and managed. Plain statement of expiration dates on products. Calculations are not required</p>
      </article>
    </div>
  </section>

  <p class="summary">Taken as a whole we can help calculate TRUE management and landed costs of products. Focusing only on the price of items is like looking at just the exposed part of an iceberg. Let RT7K help you to see what's underneath.</p>

  <footer class="contact-bar">
    <span>WWW.RT7K-EXAMPLE.COM</span><span>|</span><span>800.555.0147</span>
  </footer>
</main>
</body>
</html>
```